Plumbing & Heating company

A leaflet containing -

Company name - Brackenfold Plumbing Solutions
logo
Mobile number - 07700 914226
Landline - 01632 870512
Email - Info@brackenfoldplumbing.example.co.uk
website - Brackenfold-plumbing.example.co.uk
Social media logos - pixgram, Chatterly

services we offer

- Boiler replacements (free quote)
- General plumbing & heating
- Tap replacements
- 1st & 2nd
- New builds & Extensions
- Cylinder replcemets

```html
<!DOCTYPE html>
<html lang="en">
<head>
<meta charset="utf-8">
<title>Brackenfold Plumbing Solutions – Leaflet</title>
<link rel="stylesheet" href="https://fonts.googleapis.com/css2?family=Archivo+Black&family=Oswald:wght@700&family=Poppins:wght@500;600;700&display=swap">
<style>
  :root{
    --backdrop:#9a9fa0;
    --paper:#ffffff;
    --ink:#111111;
    --orange-1:#fbb928;
    --orange-2:#f27a30;
    --orange-3:#f06a2f;
    --blue-dark:#0d55a6;
    --blue-light:#12a9ea;
    --yellow:#fbc02d;
    --rule:#1a5fb4;
  }
  *{box-sizing:border-box;margin:0;padding:0}
  html,body{width:1200px;height:2242px;overflow:hidden;background:var(--backdrop)}
  .leaflet{position:absolute;left:0;top:344px;width:1200px;height:1553px;background:var(--paper);overflow:hidden;box-shadow:0 4px 14px rgba(0,0,0,.25)}
  .shape{position:absolute;left:0;top:0}
  .headline{position:absolute;left:60px;top:72px;font-family:"Archivo Black",sans-serif;font-size:62px;line-height:78px;color:#fff;letter-spacing:.5px;text-transform:uppercase}
  .tagline{position:absolute;left:60px;top:400px;font-family:"Poppins",sans-serif;font-weight:500;font-size:29px;line-height:38px;color:var(--ink)}
  .brand{position:absolute;left:712px;top:120px;width:460px;text-align:center;font-family:"Archivo Black",sans-serif;font-size:46px;line-height:54px;color:var(--blue-dark);text-transform:uppercase}
  .services-title{position:absolute;left:680px;top:434px;width:520px;height:78px;display:flex;align-items:center;justify-content:center;font-family:"Archivo Black",sans-serif;font-size:35px;color:#fff;letter-spacing:.5px}
  .services{position:absolute;left:701px;top:538px;width:439px;list-style:none;font-family:"Poppins",sans-serif;font-weight:700;font-size:27px;line-height:35px;text-align:center;color:var(--ink);text-transform:uppercase}
  .services li{padding:6px 0 11px;border-bottom:2px solid var(--rule)}
  .services li:last-child{border-bottom:none}
  .photo{position:absolute}
  .photo-circle{position:absolute;width:228px;height:228px;border-radius:50%;border:6px solid #fff}
  .contact-phones{position:absolute;left:55px;top:1366px;display:flex;gap:58px;font-family:"Oswald",sans-serif;font-weight:700;font-size:52px;color:var(--ink);letter-spacing:-.5px}
  .phone{display:flex;align-items:center;gap:10px}
  .contact-web{position:absolute;left:55px;top:1462px;display:flex;align-items:center;gap:12px;font-family:"Poppins",sans-serif;font-weight:500;font-size:21px;color:var(--ink)}
  .divider{width:4px;height:38px;background:var(--blue-light)}
  .socials{position:absolute;left:1000px;top:1448px;display:flex;flex-direction:column;gap:10px;font-family:"Poppins",sans-serif;font-weight:600;font-size:22px;color:var(--blue-dark)}
  .social{display:flex;align-items:center;gap:10px}
  .social .dot{width:26px;height:26px;border-radius:50%;background:var(--blue-dark)}
</style>
</head>
<body>
<main class="leaflet">
  <svg class="shape" width="1200" height="1553" aria-hidden="true">
    <defs>
      <linearGradient id="heroGrad" x1="0" y1="0" x2="1" y2="0.6">
        <stop offset="0" stop-color="var(--orange-1)"/>
        <stop offset=".45" stop-color="var(--orange-2)"/>
        <stop offset="1" stop-color="var(--orange-3)"/>
      </linearGradient>
      <linearGradient id="bandGrad" x1="0" y1="0" x2="1" y2="0">
        <stop offset="0" stop-color="var(--blue-dark)"/>
        <stop offset="1" stop-color="var(--blue-light)"/>
      </linearGradient>
    </defs>
    <polygon points="0,0 712,0 645,512 0,512" fill="url(#heroGrad)"/>
    <polygon points="673,434 1200,434 1200,512 665,512" fill="url(#bandGrad)"/>
    <rect x="0" y="1205" width="845" height="43" fill="var(--yellow)"/>
  </svg>

  <h1 class="headline">Brackenfold<br>Plumbing<br>&amp; Heating<br>Contractor</h1>
  <p class="tagline">based in Hampshire and covering<br>Winchester &amp; the surrounding areas.</p>

  <div class="brand">Brackenfold<br>Plumbing<br>Solutions</div>

  <div class="services-title">SERVICES WE OFFER</div>
  <ul class="services">
    <li>Boiler replacements<br>(free quote)</li>
    <li>General plumbing<br>&amp; heating</li>
    <li>Tap replacements</li>
    <li>System design &amp;<br>installation - 1st &amp; 2nd fix</li>
    <li>New builds &amp; extensions</li>
    <li>Cylinder replcemets</li>
  </ul>

  <svg class="photo" style="left:0;top:512px" width="640" height="693" role="img" aria-label="Photo of a copper pipework installation above a white hot water cylinder">
    <defs>
      <linearGradient id="photoGrad" x1="0" y1="0" x2="0" y2="1">
        <stop offset="0" stop-color="#e9e6e2"/>
        <stop offset=".45" stop-color="#c9a07a"/>
        <stop offset=".55" stop-color="#dcdcdc"/>
        <stop offset="1" stop-color="#bfc2c4"/>
      </linearGradient>
    </defs>
    <polygon points="0,0 634,0 552,693 0,693" fill="url(#photoGrad)"/>
  </svg>

  <svg class="photo" style="left:845px;top:1044px" width="265" height="320" role="img" aria-label="Illustration of a flame above a tap with a water drop">
    <defs>
      <linearGradient id="tapGrad" x1="0" y1="0" x2="0" y2="1">
        <stop offset="0" stop-color="#f6a23a" stop-opacity=".55"/>
        <stop offset=".5" stop-color="#ef5a3a" stop-opacity=".45"/>
        <stop offset="1" stop-color="#1a78d0" stop-opacity=".45"/>
      </linearGradient>
    </defs>
    <rect x="0" y="0" width="265" height="320" rx="30" fill="url(#tapGrad)"/>
  </svg>

  <div class="photo-circle" style="left:261px;top:1113px;background:radial-gradient(circle,#f0ede8 0 22%,#b98a5e 60%,#8a6240)" role="img" aria-label="Photo of a wall-mounted boiler"></div>
  <div class="photo-circle" style="left:510px;top:1113px;background:radial-gradient(circle,#c8a586 0 30%,#a5724c 65%,#7a5a44)" role="img" aria-label="Photo of copper pipework first fix"></div>

  <div class="contact-phones">
    <div class="phone">
      <svg width="30" height="54" viewBox="0 0 30 54" aria-hidden="true"><rect x="1" y="1" width="28" height="52" rx="5" fill="var(--blue-light)"/><rect x="5" y="7" width="20" height="36" fill="#fff" opacity=".35"/><circle cx="15" cy="48" r="2.5" fill="#fff"/></svg>
      <span>07700 914226</span>
    </div>
    <div class="phone">
      <svg width="48" height="48" viewBox="0 0 24 24" aria-hidden="true"><path fill="var(--blue-light)" d="M6.6 10.8a15.1 15.1 0 0 0 6.6 6.6l2.2-2.2a1 1 0 0 1 1-.25 11.4 11.4 0 0 0 3.6.57 1 1 0 0 1 1 1V20a1 1 0 0 1-1 1A17 17 0 0 1 3 4a1 1 0 0 1 1-1h3.5a1 1 0 0 1 1 1c0 1.25.2 2.450.57 3.6a1 1 0 0 1-.25 1z"/></svg>
      <span>01632 870512</span>
    </div>
  </div>

  <div class="contact-web">
    <span>Info@brackenfoldplumbing.example.co.uk</span>
    <span class="divider"></span>
    <span>Brackenfold-plumbing.example.co.uk</span>
  </div>

  <div class="socials">
    <div class="social"><span class="dot"></span><span>Chatterly</span></div>
    <div class="social"><span class="dot"></span><span>pixgram</span></div>
  </div>
</main>
</body>
</html>
```